Ilse Brandauer - Entwicklung für Menschen und Organisationen
Zielgruppe
Ich biete Organisationsentwicklungen, Coachings, Teamentwicklungen, Moderationen, Führungskräfteentwicklung, Konfliktklärung und Seminare an.
Meine Zielgruppe sind Vorstände, Geschäftsführer, Personaler, Führungskräfte und andere 'Entscheider'.
Aufgabenstellung
Das Format soll in ein DIN lang Kuvert passen, jedoch gerne nicht das klassische zweifach-gefaltete A4 sein.
Es soll zu meinem Logo und den Druckstücken passen.
Es soll herauskommen, dass alle Leistungen in der Organisationsentwicklung enthalten sein können, diese jedoch auch jeweils einzeln angeboten werden können.
Ich benötige die Broschüre als "offene" Datei, da ich in naher Zukunft die Geschäftsräume wechsele.

```html
<!DOCTYPE html>
<html lang="de">
<head>
<meta charset="utf-8">
<title>Ilse Brandauer – Faltblatt Außenseite</title>
<link href="https://fonts.googleapis.com/css2?family=Open+Sans:wght@400;600;700&display=swap" rel="stylesheet">
<style>
  :root {
    --paper: #ffffff;
    --ink: #1a1a1a;
    --brand-red: #d8232a;
    --fold-line: #3a3a3a;
    --photo-light: #eceef0;
    --photo-mid: #d9d6d3;
    --photo-warm: #cdbfb2;
  }
  html, body {
    margin: 0;
    padding: 0;
    overflow: hidden;
  }
  body {
    width: 1200px;
    height: 795px;
    background: var(--paper);
    font-family: "Open Sans", Arial, sans-serif;
    color: var(--ink);
  }
  .brochure {
    position: relative;
    width: 1200px;
    height: 795px;
    overflow: hidden;
    background: var(--paper);
    border-top: 1px solid var(--fold-line);
    box-sizing: border-box;
  }
  .fold {
    position: absolute;
    top: 0;
    bottom: 0;
    width: 1px;
    background: var(--fold-line);
  }
  .fold--first { left: 401px; }
  .fold--second { left: 801px; }

  /* Vorteile panel */
  .benefits__title {
    position: absolute;
    left: 31px;
    top: 77px;
    margin: 0;
    font-weight: 600;
    font-size: 26.5px;
    line-height: 34px;
    letter-spacing: 1.3px;
    text-transform: uppercase;
    white-space: nowrap;
  }
  .benefit {
    position: absolute;
    left: 30px;
    width: 340px;
  }
  .benefit__marker {
    position: absolute;
    left: 0;
    top: 0;
    width: 36px;
    height: 36px;
    border-radius: 3px;
    background: var(--brand-red);
  }
  .benefit__heading {
    position: relative;
    top: -6px;
    margin: 0 0 7px 61px;
    font-size: 13.5px;
    font-weight: 700;
    line-height: 18px;
    white-space: nowrap;
  }
  .benefit__text {
    position: relative;
    top: -6px;
    margin: 0 0 0 61px;
    width: 279px;
    font-size: 13px;
    line-height: 17.6px;
    letter-spacing: -0.05px;
    text-align: justify;
    hyphens: manual;
  }
  .benefit--one { top: 197px; }
  .benefit--two { top: 330px; }
  .benefit--three { top: 518px; }

  /* Kontakt panel */
  .contact__title {
    position: absolute;
    left: 540px;
    top: 110px;
    margin: 0;
    font-weight: 600;
    font-size: 27px;
    line-height: 34px;
    letter-spacing: 1.3px;
    white-space: nowrap;
  }
  .contact {
    position: absolute;
    left: 543px;
    top: 192px;
    font-size: 14px;
    line-height: 20px;
  }
  .contact__name {
    margin: 0 0 8px;
    font-weight: 700;
  }
  .contact__address {
    margin: 0 0 21px;
    font-style: normal;
  }
  .contact__list {
    margin: 0 0 20px;
    padding: 0;
    list-style: none;
  }
  .contact__list li {
    display: flex;
  }
  .contact__label {
    width: 24px;
  }

  /* Titel panel */
  .cover__photo {
    position: absolute;
    left: 831px;
    top: 31px;
    width: 340px;
    height: 741px;
    background:
      radial-gradient(ellipse 55% 30% at 62% 38%, var(--photo-mid), transparent 70%),
      radial-gradient(ellipse 50% 25% at 55% 72%, var(--photo-warm), transparent 70%),
      linear-gradient(180deg, var(--photo-light) 0%, #e4e4e4 60%, #e8eaec 100%);
  }
  .cover__brand {
    position: absolute;
    left: 868px;
    top: 130px;
    margin: 0;
    font-size: 32px;
    line-height: 40px;
    font-weight: 600;
    color: var(--brand-red);
    white-space: nowrap;
  }
</style>
</head>
<body>
<main class="brochure">
  <div class="fold fold--first"></div>
  <div class="fold fold--second"></div>

  <section class="benefits">
    <h2 class="benefits__title">Ihre Vorteile durch<br>meine Begleitung</h2>

    <article class="benefit benefit--one">
      <span class="benefit__marker"></span>
      <h3 class="benefit__heading">Individuell, ganz nach Ihren Bedarf</h3>
      <p class="benefit__text">Menschen und Unternehmen sind einzigartig. In diesem Bewusstsein konzipiere ich jeden Prozess ganz individuell nach Ihrer aktuel&shy;len Situation.</p>
    </article>

    <article class="benefit benefit--two">
      <span class="benefit__marker"></span>
      <h3 class="benefit__heading">Die Menschen stets im Fokus</h3>
      <p class="benefit__text">Erfolgreich können Unternehmen nur werden und sein, wenn deren Mitarbeiter motiviert und engagiert sind. Um dies zu erreichen, müssen sie beteiligt und informiert sein. Ich sorge durch die konsequente Einbindung Ihrer Mitarbeiter für nachhaltigen Erfolg Ihrer Prozesse.</p>
    </article>

    <article class="benefit benefit--three">
      <span class="benefit__marker"></span>
      <h3 class="benefit__heading">Ihre Ressourcen führen zum Erfolg</h3>
      <p class="benefit__text">Meine Arbeiten zielt darauf ab, mit geeig&shy;neten Modellen, Methoden und Prozessen, die Ressourcen und Fähigkeiten von Ihren Mitarbeitern und Ihnen zu nutzen, um mit Ihnen die beste und authentischste Lösung für Ihr Unternehmen zu entwickeln.</p>
    </article>
  </section>

  <section class="contact-panel">
    <h2 class="contact__title">KONTAKTDATEN</h2>
    <div class="contact">
      <p class="contact__name">Ilse Brandauer</p>
      <address class="contact__address">Birkenweg 12<br>90402 Nürnberg</address>
      <ul class="contact__list">
        <li><span class="contact__label">T</span>0911 / 4830 2215</li>
        <li><span class="contact__label">H</span>0170 / 38 61 704</li>
        <li><span class="contact__label">F</span>0911/ 4830 2216</li>
      </ul>
      <ul class="contact__list">
        <li><span class="contact__label">M</span>post@ilse-brandauer.de</li>
        <li><span class="contact__label">W</span>www.ilse-brandauer.de</li>
      </ul>
    </div>
  </section>

  <section class="cover">
    <div class="cover__photo" role="img" aria-label="Foto weißer Orchideenblüten vor hellgrauem Hintergrund"></div>
    <h1 class="cover__brand">Ilse Brandauer</h1>
  </section>
</main>
</body>
</html>
```